label for health supplement

The supplement targets cardiovascular diseases.
The size is: 146 mm and height 54 mm
The name of the product is: Vellamor Plus
I will need the source file as we'll probably be required to make modifications to be fully NRRB compliant.
It should contain the following text lines on it:

VELLAMOR PLUS
HEALTH FOOD GMP & ISO9001 COMPLIANT
DIETARY SUPPLEMENT
60 CAPSULES

Foundation for Longer Life
Essential For Cardiovascular Health
Scientifically-designed supplement
Lowers cholesterol level

Suggested Use
Take one or two capsules daily, or as directed by a physician.

Not intended for children or pregnant women.
Consult a healthcare practitioner prior to use.
Store in a cool dry place away from children
These statements have not been evaluated by the National Remedy Review Board. This product is not intended to diagnose, treat, cure or prevent any disease.

The part below should look like:

http://3.cd.pinmorrow.net/-7k2hQwZbXcv/UXyzT4rMnoP/BBBBBBBBByQ/QmprKo9PLzw/s1600/8-oz-nutritional-panel.jpg

Supplement Facts
Serving Size: 2 Softgels
Servings per Container: 45
Amount Per Serving % Daily Value
Calories 5
Calories from Fat 5 3%*
Total Fat 0.5 g
Saturated Fat 0 g 0%*
Vitamin E (as d-alpha tocopherol) 1 IU 3%
Vitamin A 90-95 IU 90 4%-8%
Vitamin D 0-5 IU 0 (5) 0% - 1%
Omega-3 Fatty Acids 140 mg *
EPA (Eicosapentaenoic Acid) 45 mg *
DHA (Docosahexaenoic Acid) 70 mg *
Other Omega-3s 25 mg *
*Daily value not established.

Target Market(s)

The target market is made by people from 35-80 years old since they are the most suffering from cardiovascular diseases.

Industry/Entity Type

Healthcare

Colors

Designer to choose colors to be used in the design.

Requirements
Must have
• I must receive the source file since I will probably need to make more modifications in the future to it based on registration requirements.

```html
<!DOCTYPE html>
<html lang="en">
<head>
<meta charset="utf-8">
<title>Vellamor Plus – Supplement Label</title>
<link href="https://fonts.googleapis.com/css2?family=Archivo+Narrow:wght@400;700&family=Oswald:wght@600&family=Tinos&family=Arimo:wght@400;700&display=swap" rel="stylesheet">
<style>
  :root {
    --backdrop: #727170;
    --label-white: #ffffff;
    --panel-light: #f2f2f2;
    --panel-mid: #dcdcdc;
    --brand-red: #d9241f;
    --brand-black: #1d1a18;
    --ink: #1a1a1a;
    --rule: #222;
  }
  * { box-sizing: border-box; margin: 0; padding: 0; }
  html, body { width: 1200px; height: 665px; overflow: hidden; }
  body { background: var(--backdrop); position: relative; font-family: "Arimo", Arial, sans-serif; color: var(--ink); }

  .label {
    position: absolute; left: 105px; top: 150px; width: 990px; height: 366px;
    border-radius: 22px; overflow: hidden; background: var(--label-white);
    box-shadow: 0 8px 10px rgba(0,0,0,.35);
  }
  .panel { position: absolute; top: 0; height: 100%; }

  /* Left: claims and directions */
  .panel--info {
    left: 0; width: 257px; padding: 13px 12px 0 13px;
    font-family: "Archivo Narrow", "Arial Narrow", sans-serif; font-size: 13px; line-height: 19px;
    background: linear-gradient(90deg, #fff 0%, #f7f7f7 85%, #e6e6e6 100%);
  }
  .claims { list-style: none; margin-bottom: 18px; }
  .use-heading { color: var(--brand-red); font-weight: 700; font-size: 13px; }
  .directions p { text-align: justify; }
  .disclaimer {
    position: absolute; left: 13px; top: 313px; width: 232px; height: 38px;
    border: 1px solid #555; font-size: 11.5px; line-height: 15px;
    text-align: center; padding-top: 3px;
  }

  /* Centre: brand face */
  .panel--front {
    left: 257px; width: 420px;
    background: radial-gradient(ellipse at 50% 55%, #ffffff 0%, var(--panel-light) 45%, var(--panel-mid) 100%);
    text-align: center;
  }
  .swoosh { position: absolute; left: 0; top: 0; width: 420px; height: 62px; display: block; }
  .product-name {
    position: absolute; left: 0; right: 0; top: 66px;
    font-family: "Oswald", "Impact", sans-serif; font-weight: 600;
    font-size: 58px; line-height: 68px; color: var(--brand-red);
    transform: scaleX(.92); letter-spacing: 1px;
  }
  .compliance {
    position: absolute; left: 0; right: 0; top: 150px;
    font-family: "Tinos", "Times New Roman", serif; font-size: 20px; line-height: 31px; letter-spacing: .5px;
  }
  .category {
    position: absolute; left: 45px; top: 229px; width: 340px; height: 54px;
    border: 2px solid var(--brand-red); border-radius: 50%;
    font-family: "Tinos", "Times New Roman", serif; font-size: 20px; line-height: 50px; letter-spacing: .5px;
  }
  .count {
    position: absolute; left: 21px; top: 312px; width: 380px; height: 38px;
    background: var(--brand-red); color: #fff;
    font-weight: 700; font-size: 18px; line-height: 38px; letter-spacing: .5px;
  }

  /* Right: supplement facts */
  .panel--facts {
    left: 677px; width: 313px;
    background: linear-gradient(90deg, #e4e4e4 0%, #fafafa 8%, #fff 100%);
  }
  .facts {
    position: absolute; left: 26px; top: 12px; width: 262px; height: 340px;
    border: 2px solid var(--rule); padding: 2px 7px 0 7px; font-size: 11.5px; line-height: 17px;
  }
  .facts__title { font-weight: 700; font-size: 25.5px; line-height: 31px; letter-spacing: -.2px; }
  .facts__serving { font-size: 10.5px; line-height: 12px; }
  .facts__bar { height: 7px; background: var(--rule); margin: 4px 0 2px; }
  .facts__row { display: flex; justify-content: space-between; border-bottom: 1px solid #888; }
  .facts__row--head { font-weight: 700; border-bottom: 2px solid var(--rule); }
  .facts__row--dv { justify-content: flex-end; font-weight: 700; border-bottom: 2px solid var(--rule); }
  .facts__row--sub { padding-left: 14px; }
  .facts__note { position: absolute; left: 0; right: 0; bottom: 0; border-top: 2px solid var(--rule); padding: 1px 7px; font-size: 11.5px; }
</style>
</head>
<body>
  <div class="label">
    <section class="panel panel--info">
      <ul class="claims">
        <li>Foundation for Longer Life</li>
        <li>Essential For Cardiovascular Health</li>
        <li>Scientifically-designed supplement</li>
        <li>Lowers cholesterol level</li>
      </ul>
      <div class="directions">
        <h3 class="use-heading">SUGGESTED USE</h3>
        <p>Take one or two capsules daily, or as directed by a physician.</p>
        <p>Not intended for children or pregnant women.</p>
        <p>Consult a healthcare practitioner prior to use.</p>
        <p>Store in a cool dry place away from children These statements have not been evaluated by the National Remedy Review Board.</p>
      </div>
      <div class="disclaimer">This product is not intended to diagnose, treat, cure or prevent any disease.</div>
    </section>

    <section class="panel panel--front">
      <svg class="swoosh" viewBox="0 0 420 62" preserveAspectRatio="none" aria-hidden="true">
        <path d="M205 0 L420 0 L420 52 Q350 14 205 0 Z" fill="var(--brand-black)"/>
        <path d="M0 0 L420 0 L420 5 Q260 6 160 26 Q70 44 0 62 Z" fill="var(--brand-red)"/>
      </svg>
      <h1 class="product-name">VELLAMOR PLUS</h1>
      <p class="compliance">HEALTH FOOD GMP<br>&amp; ISO 9001 COMPLIANT</p>
      <p class="category">DIETARY SUPPLEMENT</p>
      <p class="count">60 CAPSULES</p>
    </section>

    <section class="panel panel--facts">
      <div class="facts">
        <h2 class="facts__title">Supplement Facts</h2>
        <p class="facts__serving">Serving Size: 2 Softgels<br>Servings per Container: 45</p>
        <div class="facts__bar"></div>
        <div class="facts__row facts__row--head"><span>Amount Per Serving</span></div>
        <div class="facts__row facts__row--dv"><span>% Daily Value</span></div>
        <div class="facts__row"><span>Calories 5</span></div>
        <div class="facts__row facts__row--sub"><span>Calories from Fat</span><span>5 3%*</span></div>
        <div class="facts__row"><span>Total Fat 0.5 g</span></div>
        <div class="facts__row"><span>Saturated Fat 0 g</span><span>0%*</span></div>
        <div class="facts__row"><span>Vitamin E (as d-alpha tocopherol) 1 IU</span><span>3%</span></div>
        <div class="facts__row"><span>Vitamin A 90-95 IU 90</span><span>4%-8%</span></div>
        <div class="facts__row"><span>Vitamin D 0-5 IU 0 (5)</span><span>0% - 1%</span></div>
        <div class="facts__row"><span>Omega-3 Fatty Acids 140 mg *</span></div>
        <div class="facts__row"><span>EPA (Eicosapentaenoic Acid) 45 mg *</span></div>
        <div class="facts__row"><span>DHA (Docosahexaenoic Acid) 70 mg *</span></div>
        <div class="facts__row"><span>Other Omega-3s 25 mg *</span></div>
        <p class="facts__note">*Daily value not established.</p>
      </div>
    </section>
  </div>
</body>
</html>
```